design an extra page for our profile

we are looking for someone to create another page like the attached but with the below changes:
heading changed to (Construction)
icons changed and names to reflect new services i.e
- Residential Building
- Commercial Building
- Landscaping
- Concrete
- Painting

the very bottom of the page is to stay the same with our office info

```html
<!DOCTYPE html>
<html lang="en">
<head>
<meta charset="utf-8">
<title>Construction – Services Page</title>
<link href="https://fonts.googleapis.com/css2?family=Montserrat:wght@600;700;800&family=Open+Sans:wght@600&display=swap" rel="stylesheet">
<style>
  :root {
    --page-bg: #4a4a4a;
    --navy: #173a85;
    --navy-deep: #12337d;
    --pill: #4d87c9;
    --rule: #4d87c9;
    --sky-light: #e9f1f8;
    --sky-mid: #cfdeec;
    --icon: #1f3d8c;
    --label: #2b2b2b;
    --white: #ffffff;
  }
  * { margin: 0; padding: 0; box-sizing: border-box; }
  html, body { width: 1200px; height: 1000px; overflow: hidden; background: var(--page-bg); }
  .flyer {
    position: absolute; left: 263px; top: 63px; width: 675px; height: 874px;
    background: var(--sky-light); overflow: hidden;
    font-family: "Montserrat", sans-serif;
  }
  .header { position: absolute; left: 0; top: 0; width: 100%; height: 195px; background: var(--navy); }
  .header-rule { position: absolute; left: 42px; right: 42px; top: 52px; height: 3px; background: var(--rule); }
  .title-pill {
    position: absolute; left: 161px; top: 31px; width: 353px; height: 43px;
    background: var(--pill); border-radius: 22px;
    color: var(--white); font-weight: 800; font-size: 33px; letter-spacing: 0.5px;
    display: flex; align-items: center; justify-content: center;
  }
  .intro {
    position: absolute; left: 0; top: 92px; width: 100%; text-align: center;
    color: var(--white); font-family: "Open Sans", sans-serif; font-weight: 600;
    font-size: 20.5px; line-height: 29px; letter-spacing: 0.3px;
  }
  .skyline {
    position: absolute; left: 0; top: 195px; width: 100%; height: 612px;
    background: linear-gradient(180deg, #f1f6fb 0%, var(--sky-light) 40%, var(--sky-mid) 100%);
  }
  .service { position: absolute; width: 240px; text-align: center; }
  .service svg { display: block; margin: 0 auto; }
  .service-label {
    display: block; margin-top: 18px; color: var(--label);
    font-weight: 700; font-size: 19px; letter-spacing: 0.6px; white-space: nowrap;
  }
  .divider { position: absolute; width: 3px; background: var(--rule); }
  .site-photo {
    position: absolute; left: 41px; top: 577px; width: 593px; height: 229px;
    background: linear-gradient(180deg, #3f7fd0 0%, #8fb9e4 45%, #b9b5ab 70%, #b35a45 100%);
  }
  .footer { position: absolute; left: 0; top: 807px; width: 100%; height: 67px; background: var(--navy-deep); color: var(--white); }
  .brand {
    position: absolute; left: 40px; top: 21px; display: flex; align-items: center; gap: 6px;
    font-weight: 700; font-size: 17px;
  }
  .brand-dot { width: 10px; height: 10px; border-radius: 50%; background: var(--white); }
  .contact-top { position: absolute; left: 149px; top: 13px; width: 483px; height: 16px; font-size: 12px; font-weight: 600; white-space: nowrap; }
  .contact-top strong { font-weight: 700; }
  .contact-top .address { position: absolute; left: 194px; top: 0; font-size: 12.5px; }
  .footer-rule { position: absolute; left: 149px; right: 43px; top: 32px; height: 1px; background: var(--white); }
  .contact-bottom {
    position: absolute; left: 149px; top: 38px; width: 483px;
    display: flex; justify-content: space-between; align-items: center;
    font-size: 10.5px; font-weight: 700; letter-spacing: 0.1px; white-space: nowrap;
  }
  .contact-bottom .sep { font-weight: 600; }
</style>
</head>
<body>
<main class="flyer">
  <header class="header">
    <div class="header-rule"></div>
    <h1 class="title-pill">CONSTRUCTION</h1>
    <p class="intro">AS NEW TENANTS TO THE BUILDING AND AS A WAY<br>OF INTRODUCING OURSELVES WE WOULD LIKE TO OFFER<br>A 10% DISCOUNT ON ANY OF THE BELOW SERVICES.</p>
  </header>

  <div class="skyline" role="img" aria-label="Faint city skyline of high-rise towers"></div>

  <section class="services">
    <div class="service" style="left:-3px; top:222px;">
      <svg width="100" height="88" viewBox="0 0 100 88" fill="none" stroke="var(--icon)" stroke-width="3" stroke-linejoin="round">
        <rect x="4" y="52" width="92" height="14"/>
        <path d="M66 52 V26 H84 L94 40 V52"/><path d="M72 30 H82 L88 40 H72 Z"/>
        <ellipse cx="34" cy="32" rx="28" ry="17" transform="rotate(-15 34 32)"/>
        <circle cx="22" cy="72" r="8"/><circle cx="78" cy="72" r="8"/>
      </svg>
      <span class="service-label">CONCRETE</span>
    </div>
    <div class="divider" style="left:220px; top:232px; height:116px;"></div>

    <div class="service" style="left:224px; top:222px;">
      <svg width="100" height="88" viewBox="0 0 100 88" fill="none" stroke="var(--icon)" stroke-width="3" stroke-linejoin="round">
        <circle cx="30" cy="12" r="6"/>
        <path d="M34 56 L50 18 L60 32 L66 24 L84 56"/>
        <ellipse cx="16" cy="30" rx="9" ry="12"/><path d="M16 42 V62"/>
        <path d="M6 62 H94 M10 74 H60 M70 74 H94 M20 84 H80"/>
      </svg>
      <span class="service-label">LANDSCAPING</span>
    </div>
    <div class="divider" style="left:467px; top:232px; height:116px;"></div>

    <div class="service" style="left:445px; top:222px;">
      <svg width="100" height="88" viewBox="0 0 100 88" fill="none" stroke="var(--icon)" stroke-width="3" stroke-linejoin="round">
        <path d="M6 40 L50 4 L94 40"/><path d="M70 20 V8 H80 V28"/>
        <path d="M16 32 V86 H84 V32"/>
        <rect x="38" y="48" width="24" height="38"/><path d="M24 50 H32 V66 H24 Z"/>
      </svg>
      <span class="service-label">PAINTING</span>
    </div>

    <div class="service" style="left:80px; top:406px;">
      <svg width="90" height="86" viewBox="0 0 90 86" fill="none" stroke="var(--icon)" stroke-width="3" stroke-linejoin="round">
        <rect x="22" y="4" width="40" height="80"/><rect x="4" y="20" width="18" height="64"/><rect x="62" y="20" width="24" height="64"/>
        <path d="M30 14 H54 M30 26 H54 M30 38 H54 M30 50 H54 M10 32 H16 M10 46 H16 M10 60 H16 M68 32 H80 M68 46 H80 M68 60 H80"/>
        <rect x="34" y="64" width="16" height="20"/>
      </svg>
      <span class="service-label">RESIDENTIAL BUILDING</span>
    </div>
    <div class="divider" style="left:342px; top:417px; height:116px;"></div>

    <div class="service" style="left:369px; top:396px;">
      <svg width="100" height="96" viewBox="0 0 100 96" fill="none" stroke="var(--icon)" stroke-width="3" stroke-linejoin="round">
        <rect x="4" y="6" width="44" height="88"/>
        <path d="M12 18 H40 M12 32 H40 M12 46 H40 M12 60 H40"/>
        <path d="M48 40 L74 22 L96 40 V94 H48"/><path d="M58 54 H88 M58 68 H88"/>
        <circle cx="14" cy="80" r="6"/><circle cx="88" cy="80" r="6"/><rect x="64" y="78" width="14" height="16"/>
      </svg>
      <span class="service-label">COMMERCIAL BUILDING</span>
    </div>
  </section>

  <div class="site-photo" role="img" aria-label="Photo of apartment blocks under construction with tower cranes against a blue sky"></div>

  <footer class="footer">
    <div class="brand"><span class="brand-dot"></span><span>Kestrel</span></div>
    <p class="contact-top"><strong>HOME OFFICE:</strong> 1300 22 4891 <span class="address">Suite 4.02, 8 Harbour Lane Norwest</span></p>
    <div class="footer-rule"></div>
    <p class="contact-bottom"><span>WWW.KESTREL-SERVICES.COM.AU</span><span>SYDNEY</span><span class="sep">|</span><span>CANBERRA</span><span class="sep">|</span><span>BRISBANE</span><span class="sep">|</span><span>MELBOURNE</span></p>
  </footer>
</main>
</body>
</html>
```